Flyer for photo scanning business

Hello,
I need a flyer created for my business that would be suitable for print, to drop in letterboxes in my local community.

I would like the flyer to convey very simply the services I offer which is scanning negatives, slides and VHS tapes to digital files.
Hopefully it can make it look like an easy process, as people are often daunted by the task of sorting through old photos so they don't always get around to having them scanned.

I have a pinned facebook post that can be used by the designer to reference my services. Pricing does not need to be included on the flyer.
http://facebook.com/brightvaleimaging

Target Market(s)

Parents & Grandparents

Requirements
Must have
• Must make my services look simple! Refer to pinned facebook post for detailed outline of my services.

I would like to flyer to point towards my contact details -
www.brightvale.com
Margot 0478 219 836

Colours in line with my logo/brand (uploaded to brief).
Nice to have
• Stock images of 35mm film negatives, 8mm film, VHS tapes, or Lumavert slides would be worth including. I have also uploaded a mockup of the USB sticks that I provide with digitised images.
Should not have
• no prices needed,

```html
<!DOCTYPE html>
<html lang="en">
<head>
<meta charset="UTF-8">
<title>Brightvale Imaging – Flyer</title>
<link href="https://fonts.googleapis.com/css2?family=Montserrat:wght@400;500;600;700;800&display=swap" rel="stylesheet">
<style>
  :root {
    --brand-dark: #2a62a0;
    --brand-mid: #3f86c4;
    --brand-light: #63ade0;
    --ink: #1f2329;
    --soft-grey: #f0f1f3;
    --page-bg: #e4e5e7;
    --white: #ffffff;
  }
  * { margin: 0; padding: 0; box-sizing: border-box; }
  html, body { width: 1200px; height: 1083px; overflow: hidden; }
  body {
    background: var(--page-bg);
    font-family: "Montserrat", sans-serif;
    color: var(--ink);
    position: relative;
  }
  .flyer {
    position: absolute;
    left: 231px; top: 20px;
    width: 738px; height: 1043px;
    background: var(--white);
    overflow: hidden;
  }
  .backdrop { position: absolute; inset: 0; }

  .brand {
    position: absolute; left: 50px; top: 70px; width: 310px;
    text-align: center; color: var(--brand-dark);
  }
  .brand-mark {
    width: 56px; height: 56px; border-radius: 50%;
    background: var(--brand-mid); margin: 0 auto 16px;
  }
  .brand-name {
    font-weight: 500; font-size: 27px; letter-spacing: 6px; line-height: 1.2;
    color: var(--ink);
  }
  .brand-sub {
    display: flex; align-items: center; justify-content: center; gap: 12px;
    margin-top: 4px; font-weight: 500; font-size: 17px; letter-spacing: 5px;
  }
  .brand-sub::before, .brand-sub::after {
    content: ""; width: 56px; height: 1.5px; background: var(--brand-dark);
  }

  .headline {
    position: absolute; left: 40px; top: 560px; width: 320px;
    color: var(--brand-dark); font-weight: 800; font-size: 22px; line-height: 1.2;
    padding-bottom: 16px; border-bottom: 1.5px solid var(--brand-dark);
  }

  .steps { position: absolute; left: 40px; top: 690px; width: 430px; list-style: none; }
  .step { margin-bottom: 16px; }
  .step-tag {
    display: inline-block; background: var(--brand-dark); color: var(--white);
    font-weight: 700; font-size: 19px; padding: 2px 34px 2px 10px;
    clip-path: polygon(0 0, 100% 0, 86% 100%, 0 100%);
  }
  .step-text {
    display: flex; gap: 6px; margin-top: 6px;
    font-size: 11.5px; line-height: 1.4; color: var(--ink);
  }
  .step-text svg { flex: 0 0 12px; margin-top: 2px; }

  .about {
    position: absolute; left: 380px; top: 505px; width: 320px; height: 200px;
    background: linear-gradient(160deg, var(--brand-light), var(--brand-dark));
    border-radius: 0 0 14px 14px; color: var(--white);
    padding: 26px 22px 14px; font-weight: 600; font-size: 13.5px; line-height: 1.3;
  }
  .about p + p { margin-top: 8px; }

  .footer { position: absolute; left: 0; bottom: 0; width: 738px; height: 80px; }
  .footer-web {
    position: absolute; left: 40px; bottom: 30px; color: var(--white);
    font-weight: 600; font-size: 17px; display: flex; align-items: center; gap: 10px;
  }
  .footer-contact {
    position: absolute; right: 40px; bottom: 22px; color: var(--white);
    font-weight: 800; font-size: 24px; display: flex; align-items: center; gap: 14px;
    letter-spacing: 0.5px;
  }
</style>
</head>
<body>
<main class="flyer">
  <svg class="backdrop" width="738" height="1043" viewBox="0 0 738 1043">
    <defs>
      <linearGradient id="filmTone" x1="0" y1="0" x2="1" y2="1">
        <stop offset="0" stop-color="#d9d4cc"/>
        <stop offset="0.5" stop-color="#6b4630"/>
        <stop offset="1" stop-color="#2a2522"/>
      </linearGradient>
      <linearGradient id="slideTone" x1="0" y1="0" x2="1" y2="1">
        <stop offset="0" stop-color="#efe9dc"/>
        <stop offset="1" stop-color="#b9b2a4"/>
      </linearGradient>
      <linearGradient id="reelTone" x1="0" y1="0" x2="1" y2="1">
        <stop offset="0" stop-color="#e3e4e6"/>
        <stop offset="1" stop-color="#8e8a88"/>
      </linearGradient>
    </defs>
    <circle class="logo-disc" cx="190" cy="110" r="280" fill="var(--soft-grey)"/>
    <path class="photo-film" role="img" aria-label="Photo of assorted 35mm film canisters and rolls"
      d="M420 150 Q500 230 490 350 Q482 450 420 510 L738 520 L738 190 Z" fill="url(#filmTone)"/>
    <path d="M450 80 Q520 320 350 430" fill="none" stroke="var(--brand-mid)" stroke-width="1"/>
    <path d="M340 500 Q540 600 738 540" fill="none" stroke="var(--brand-mid)" stroke-width="1"/>
    <circle class="photo-slides" role="img" aria-label="Photo of a box of Lumavert slides and a slide viewer"
      cx="200" cy="400" r="135" fill="url(#slideTone)" stroke="var(--brand-mid)" stroke-width="1"/>
    <ellipse class="photo-reel" role="img" aria-label="Photo of a film reel with unwound cine film"
      cx="590" cy="860" rx="100" ry="80" fill="url(#reelTone)"/>
    <polygon points="0,963 390,963 360,1043 0,1043" fill="var(--brand-light)"/>
    <polygon points="390,963 738,963 738,1043 360,1043" fill="var(--brand-dark)"/>
  </svg>

  <div class="brand">
    <div class="brand-mark"></div>
    <div class="brand-name">BRIGHTVALE</div>
    <div class="brand-sub">IMAGING</div>
  </div>

  <section class="about">
    <p>Brightvale Imaging scans photo negatives, slides and video tapes. Images that haven’t been seen in years are digitised and brought back to life to enjoy again.</p>
    <p>Brightvale is run by a TV &amp; Broadcast professional based at home in the Ashgrove Hills.</p>
  </section>

  <h1 class="headline">I promise to make it very easy for you to keep your precious memories forever.</h1>

  <ol class="steps">
    <li class="step">
      <span class="step-tag">STEP 1</span>
      <p class="step-text"><svg width="12" height="12" viewBox="0 0 12 12"><circle cx="6" cy="6" r="5.3" fill="none" stroke="var(--brand-dark)"/><path d="M3.5 6.2l1.7 1.6 3.3-3.4" fill="none" stroke="var(--brand-dark)"/></svg>Find your old negatives or tapes and organise them as much or as little as you want.</p>
    </li>
    <li class="step">
      <span class="step-tag">STEP 2</span>
      <p class="step-text"><svg width="12" height="12" viewBox="0 0 12 12"><circle cx="6" cy="6" r="5.3" fill="none" stroke="var(--brand-dark)"/><path d="M3.5 6.2l1.7 1.6 3.3-3.4" fill="none" stroke="var(--brand-dark)"/></svg>Contact me here or email margot@brightvale.com and I will come and collect these from your home in the hills area.</p>
    </li>
    <li class="step">
      <span class="step-tag">STEP 3</span>
      <p class="step-text"><svg width="12" height="12" viewBox="0 0 12 12"><circle cx="6" cy="6" r="5.3" fill="none" stroke="var(--brand-dark)"/><path d="M3.5 6.2l1.7 1.6 3.3-3.4" fill="none" stroke="var(--brand-dark)"/></svg>Once completed (usually within a few days) I will drop back your box of memories with a USB stick containing high resolution JPEG files. Contactless payment will be processed when I arrive.</p>
    </li>
  </ol>

  <footer class="footer">
    <div class="footer-web">
      <svg width="16" height="16" viewBox="0 0 16 16" fill="none" stroke="currentColor" stroke-width="1.2"><circle cx="8" cy="8" r="7"/><ellipse cx="8" cy="8" rx="3" ry="7"/><path d="M1 8h14M2.5 4.5h11M2.5 11.5h11"/></svg>
      www.Brightvale.com
    </div>
    <div class="footer-contact">
      <span>MARGOT</span>
      <svg width="30" height="30" viewBox="0 0 30 30"><circle cx="15" cy="15" r="14" fill="var(--white)"/><path d="M10.5 8.5l3 3-1.6 1.8c1 2 2.6 3.6 4.6 4.6l1.8-1.6 3 3-2 2c-5 0-10.8-5.8-10.8-10.8z" fill="var(--brand-mid)"/></svg>
      <span>0478 219 836</span>
    </div>
  </footer>
</main>
</body>
</html>
```